Website Graphic Layout

We are looking for someone to provide a crisp clean layout for our new website design.
The site is runs on Drupal & we like the 4 column layout
We think that the current site is a bit cluttered & could be a bit cleaner.

http://www.tovaquen.org/volunteer-abroad

We like the following website as examples as they are quite clean with a large header image & sub areas to add things such as news testimonials etc

http://brastik.com/
http://www.quorvan.com/ie/
http://lantrevoda.org/
http://www.kelvasp.com/

```html
<!DOCTYPE html>
<html lang="en">
<head>
<meta charset="utf-8">
<title>Tovaquen Volunteer Abroad</title>
<link href="https://fonts.googleapis.com/css2?family=Signika:wght@300;400;600&family=Exo:ital,wght@1,600;1,700&display=swap" rel="stylesheet">
<style>
:root{
  --blue:#1b9ad8;
  --blue-dark:#2f7cc3;
  --orange:#f7a21b;
  --green:#6fa95c;
  --green-foot:#1f6d33;
  --green-deep:#0f5727;
  --grey-bg:#f1f1f1;
  --text:#444;
  --muted:#666;
}
*{box-sizing:border-box;margin:0;padding:0}
html,body{width:874px;height:1200px;overflow:hidden;background:#fff}
body{font-family:"Signika",sans-serif;color:var(--text)}
.page{position:relative;width:1020px;height:1400px;transform:scale(0.85686);transform-origin:0 0}
.abs{position:absolute}
.top-stripe{left:0;top:0;width:1020px;height:7px;background:var(--blue)}
.brand{left:40px;top:40px;display:flex;align-items:center;gap:12px}
.brand-dot{width:70px;height:70px;border-radius:50%;background:var(--blue)}
.brand-name{font-size:34px;font-weight:600;color:var(--green);line-height:1}
.brand-url{font-size:15px;color:var(--green);margin-top:6px}
.search{left:758px;top:27px;width:142px;height:19px;border:1px solid #ccc;background:#f3f3f3;font-size:10px;color:#999;padding:3px 6px}
.go{left:918px;top:27px;width:62px;height:19px;border:1px solid #ccc;background:#f3f3f3;font-size:10px;color:#999;padding:3px 8px}
.social{display:flex;gap:7px}
.social span{width:26px;height:26px;border-radius:50%;background:#9fd3ef;display:block}
.header-social{left:822px;top:66px}
.user-links{right:40px;top:106px;font-size:11px;font-style:italic;color:var(--blue);word-spacing:2px}
.nav{left:40px;top:129px;width:940px;border-top:3px solid var(--blue);border-bottom:3px solid var(--blue);height:28px;display:flex;justify-content:space-between;align-items:center;font-size:12.5px;color:#444}
.nav .sep{color:#888}
.hero{left:40px;top:162px;width:940px;height:338px;background:linear-gradient(180deg,#c9b8a4 0%,#a99480 55%,#6f6355 100%)}
.hero-caption{left:478px;top:332px;width:502px;height:108px;background:rgba(247,162,27,.92);padding:4px 10px;color:#fff;font-family:"Exo",sans-serif;font-style:italic}
.hero-caption h1{font-size:30px;font-weight:700;line-height:1.05}
.hero-caption h2{font-size:21px;font-weight:700;line-height:1.15}
.hero-caption p{font-size:13.5px;font-weight:600;margin-top:5px;line-height:1.35}
.finder{left:40px;top:500px;width:940px;height:30px;background:var(--orange);border-bottom:3px solid var(--blue)}
.finder-title{left:7px;top:5px;color:#fff;font-family:"Exo",sans-serif;font-style:italic;font-weight:700;font-size:15px}
.finder-field{top:10px;height:17px;background:var(--blue);color:#fff;font-family:"Exo",sans-serif;font-style:italic;font-weight:600;font-size:11.5px;padding:1px 6px;display:flex;justify-content:space-between}
.welcome{left:78px;top:545px;width:870px;font-size:13.2px;line-height:20.6px;color:#444}
.welcome h2{display:inline;font-family:"Exo",sans-serif;font-style:italic;font-weight:700;font-size:29px;color:var(--blue);margin-right:6px}
.welcome a{color:var(--orange);font-style:italic;text-decoration:none}
.col-head{top:688px;height:29px;color:#fff;font-size:17px;text-align:center;line-height:29px;letter-spacing:.3px}
.col-body{top:717px;height:365px;background:var(--grey-bg)}
.col-foot{top:1087px;height:79px;color:#fff;font-size:13.2px;text-align:center;line-height:15px;display:flex;flex-direction:column;justify-content:center}
.bg-blue{background:var(--blue)}.bg-green{background:var(--green)}.bg-orange{background:var(--orange)}.bg-dblue{background:var(--blue-dark)}
.testimonial{left:17px;width:200px;display:flex;gap:10px}
.thumb{width:90px;height:68px;flex:none}
.testimonial p{font-size:12px;color:#555;line-height:14px}
.testimonial i{display:block;font-size:10px;color:var(--blue);margin-top:3px}
.menu{list-style:none;text-align:center;padding-top:12px;font-size:13.5px;color:#555;letter-spacing:.2px}
.menu li{height:24px}
.menu b{color:var(--green);font-weight:400}
.video-intro{text-align:center;font-size:11.5px;line-height:13px;color:#555;padding-top:8px}
.video-main{left:20px;top:52px;width:188px;height:114px;background:#111}
.video-main-bar{left:0;bottom:0;width:188px;height:8px;background:#2a2a2a}
.vid{width:102px;height:60px;background:linear-gradient(180deg,#9aa6b3,#7a8793)}
.vid-cap{font-size:6px;text-align:center;color:#444;line-height:7px;width:102px}
.vid-cap b{color:var(--orange);font-weight:400}
.fb-card{left:10px;top:8px;width:208px;height:78px;display:flex;gap:10px}
.fb-dot{width:58px;height:58px;border-radius:50%;background:#dce9f2;flex:none}
.fb-card span{font-size:16px;color:#666;line-height:22px}
.fb-grid{left:10px;top:89px;width:208px;height:162px;background:#fff;display:grid;grid-template-columns:repeat(4,46px);gap:4px;padding:7px 6px}
.fb-grid i{display:block;height:46px;background:#a6927e}
.fb-grid i:nth-child(3n){background:#6d7f8e}
.fb-grid i:nth-child(4n+2){background:#c2a382}
.fb-likes{left:12px;top:273px;font-size:11px;color:var(--blue-dark);line-height:14px}
.fb-btn{left:166px;width:48px;height:22px;border:1px solid #cbd6e6;background:#eef3fa;font-size:11px;color:var(--blue-dark);text-align:center;line-height:20px;border-radius:2px}
.partners{left:273px;top:1198px;display:flex;gap:8px;align-items:center}
.partners span{display:block;background:#e3e3e3}
.foot-band{left:0;top:1258px;width:1020px;height:42px;background:var(--green-foot)}
.foot-links{left:50px;top:1275px;font-size:12px;color:#e6efe8;word-spacing:3px}
.footer-social{left:822px;top:1266px}
.footer-social span{background:#3e8a4f}
.foot-main{left:0;top:1300px;width:1020px;height:100px;background:var(--green-deep);color:#d7e4da;font-size:11.5px;line-height:18px}
</style>
</head>
<body>
<div class="page">
  <div class="abs top-stripe"></div>

  <header>
    <div class="abs brand">
      <div class="brand-dot"></div>
      <div>
        <div class="brand-name">Tovaquen</div>
        <div class="brand-url">www.tovaquen.org</div>
      </div>
    </div>
    <div class="abs search">Enter search</div>
    <div class="abs go">GO</div>
    <div class="abs social header-social"><span></span><span></span><span></span><span></span><span></span></div>
    <div class="abs user-links">Guest. Login &gt; &nbsp;Register &gt; &nbsp;Contact us &gt;</div>
    <nav class="abs nav">
      <span>HOME</span><span class="sep">|</span><span>STUDY ABROAD</span><span class="sep">|</span><span>VOLUNTEER ABROAD</span><span class="sep">|</span><span>DEVELOPMENT EDUCATION</span><span class="sep">|</span><span>TRAVEL AWARDS</span><span class="sep">|</span><span>VISIT IRELAND</span><span class="sep">|</span><span>ABOUT TOVAQUEN</span><span class="sep">|</span><span>COMMUNITY</span>
    </nav>
  </header>

  <section>
    <div class="abs hero" role="img" aria-label="Group photo of volunteers with local health association staff outdoors"></div>
    <div class="abs hero-caption">
      <h1>Volunteer Abroad</h1>
      <h2>Explore the world and make a difference!</h2>
      <p>Rona and Tess - Harbour College students on a Public Health internship in Jaipur, India - with the staff of the Family Health Association of Jaipur.</p>
    </div>
    <div class="abs finder">
      <div class="abs finder-title">Find Your Project</div>
      <div class="abs finder-field" style="left:160px;width:140px"><span>Region - Any</span><span>More ⋁</span></div>
      <div class="abs finder-field" style="left:320px;width:138px"><span>Type - Any</span><span>More ⋁</span></div>
      <div class="abs finder-field" style="left:480px;width:140px"><span>Duration - Any</span><span>More ⋁</span></div>
      <div class="abs finder-field" style="left:640px;width:140px;justify-content:flex-end;gap:6px"><span>Search</span><span>⋁</span></div>
    </div>
  </section>

  <section class="abs welcome">
    <h2>Welcome</h2>Tovaquen Intercultural Learning is an Irish not for profit organisation supporting local projects across the world. Our Volunteer Abroad programme involves living, working and making a difference in a local community while learning about a new culture and gaining a new perspective on global and development issues. We offer flexible and varied voluntary work and internship opportunities all year round. Our volunteers are supported by highly qualified in-country staff with years of experience in intercultural exchanges and in supporting international volunteers. <a>Find out more about our approach to short term international volunteering &nbsp;&gt;</a>
  </section>

  <!-- Testimonials -->
  <div class="abs col-head bg-blue" style="left:34px;width:229px">TESTIMONIALS</div>
  <div class="abs col-body" style="left:34px;width:229px">
    <div class="abs testimonial" style="top:9px"><div class="thumb" role="img" aria-label="Volunteers in sun hats" style="background:#b69a7a"></div><p>So you're thinking of volunteering abroad...<i>Maeve Corrin</i></p></div>
    <div class="abs testimonial" style="top:93px"><div class="thumb" role="img" aria-label="Volunteers in Vietnam" style="background:#a9a08c"></div><p>Volunteer in Vietnam: Just Do It!<i>Orla Denvy</i></p></div>
    <div class="abs testimonial" style="top:178px"><div class="thumb" role="img" aria-label="Children in India" style="background:#b77b54"></div><p>My Indian experience<i>Nia Fallow</i></p></div>
    <div class="abs testimonial" style="top:264px"><div class="thumb" role="img" aria-label="Yoga group in a courtyard" style="background:#c8b89c"></div><p>My Public Health internship in India<i>Rona Kelby</i></p></div>
  </div>
  <div class="abs col-foot bg-blue" style="left:34px;width:229px">Discover our 5 most popular destinations:<br>Vietnam, India, Guatemala,<br>Thailand and Ghana &gt;</div>

  <!-- Volunteer abroad menu -->
  <div class="abs col-head bg-green" style="left:275px;width:228px">VOLUNTEER ABROAD</div>
  <div class="abs col-body" style="left:275px;width:228px">
    <ul class="menu">
      <li>COUNTRIES <b>&gt;</b></li><li>FIND YOUR PROJECT <b>&gt;</b></li><li>UNDER-18 PROGRAMME <b>&gt;</b></li><li>INTERNSHIP PROGRAMMES <b>&gt;</b></li><li>CORPORATE VOLUNTEERING <b>&gt;</b></li><li>SCHOOL PROGRAMME <b>&gt;</b></li><li>WHY TOVAQUEN? <b>&gt;</b></li><li>IS THIS FOR ME <b>&gt;</b></li><li>WHY PAY <b>&gt;</b></li><li>HOW DO I APPLY <b>&gt;</b></li><li>FUNDRAISING <b>&gt;</b></li><li>FAQ <b>&gt;</b></li><li>CONTACT US <b>&gt;</b></li><li>NEWS <b>&gt;</b></li>
    </ul>
  </div>
  <div class="abs col-foot bg-green" style="left:275px;width:228px;font-size:13.5px;line-height:23px">ORDER A BROCHURE &gt;<br>ASK A QUESTION &gt;<br>CALL ME BACK &gt;</div>

  <!-- Videos -->
  <div class="abs col-head bg-orange" style="left:515px;width:229px">FEATURED VIDEOS</div>
  <div class="abs col-body" style="left:515px;width:229px">
    <div class="video-intro">Watch our new VIDEO<br>to find out more about<br>Tovaquen Intercultural Learning</div>
    <div class="abs video-main" role="img" aria-label="Video player with intro title"><div class="abs video-main-bar"></div></div>
    <div class="abs" style="left:11px;top:184px"><div class="vid" role="img" aria-label="Children at a classroom table"></div><div class="vid-cap">VOLUNTEERING<br>with children in shelters and<br>orphanages in VIETNAM <b>&gt;</b></div></div>
    <div class="abs" style="left:118px;top:184px"><div class="vid" role="img" aria-label="Children at a classroom table"></div><div class="vid-cap">VOLUNTEERING<br>with children in shelters and<br>orphanages in VIETNAM <b>&gt;</b></div></div>
    <div class="abs" style="left:11px;top:278px"><div class="vid" role="img" aria-label="Volunteer interview" style="background:#8c959c"></div><div class="vid-cap">VOLUNTEERING<br>in Ghana <b>&gt;</b></div></div>
    <div class="abs" style="left:118px;top:278px"><div class="vid" role="img" aria-label="Volunteer interview" style="background:#8c959c"></div><div class="vid-cap">VOLUNTEERING<br>in Ghana <b>&gt;</b></div></div>
  </div>
  <div class="abs col-foot bg-orange" style="left:515px;width:229px"><strong style="font-size:15px;font-weight:400">Lorem Ipsum</strong>Is simply dummy text of the<br>printing and typesetting &nbsp;&gt;</div>

  <!-- Community -->
  <div class="abs col-head bg-dblue" style="left:754px;width:229px">TOVAQUEN COMMUNITY</div>
  <div class="abs col-body" style="left:754px;width:229px">
    <div class="abs fb-card"><div class="fb-dot"></div><span>Tovaquen Intercultural Learning</span></div>
    <div class="abs fb-grid" role="img" aria-label="Grid of member profile pictures"><i></i><i></i><i></i><i></i><i></i><i></i><i></i><i></i><i></i><i></i><i></i><i></i></div>
    <div class="abs fb-likes">3,481 people like<br>Tovaquen Intercultural Learning</div>
    <div class="abs fb-btn" style="top:274px">Like</div>
    <div class="abs fb-btn" style="top:306px">Send</div>
  </div>
  <div class="abs col-foot bg-dblue" style="left:754px;width:229px"><strong style="font-size:15px;font-weight:400">Lorem Ipsum</strong>Is simply dummy text of the<br>printing and typesetting &nbsp;&gt;</div>

  <div class="abs partners" aria-label="Partner badges">
    <span style="width:88px;height:40px;border-radius:20px"></span>
    <span style="width:88px;height:40px;border-radius:20px"></span>
    <span style="width:88px;height:48px"></span>
    <span style="width:88px;height:40px;border-radius:20px"></span>
    <span style="width:90px;height:24px;background:#f27c4a"></span>
  </div>

  <footer>
    <div class="abs foot-band"></div>
    <div class="abs foot-links">Privacy Policy &nbsp;| &nbsp;Terms of use &nbsp;| &nbsp;About this website &nbsp;| &nbsp;Blogs</div>
    <div class="abs social footer-social"><span></span><span></span><span></span><span></span><span></span></div>
    <div class="abs foot-main">
      <div class="abs" style="left:50px;top:4px">Tovaquen Intercultural Learning,<br>14 Marlow Terrace, Hillcrest North, Corrane, County Corrane, Republic of Ireland.<br>Email: info@tovaquen.org</div>
      <div class="abs" style="left:520px;top:4px">Telephone: +353 (0)21 4900123 &nbsp;| &nbsp;Lowcall: 1850 555010<br>Fax: +353 (0)21 4900124<br>cc by-sa 2013 Tovaquen Intercultural Learning</div>
      <div class="abs" style="left:50px;top:71px">Tovaquen Intercultural Learning © copyright 2013 all rights reserved</div>
    </div>
  </footer>
</div>
</body>
</html>
```